Brochure & Business card design

Looking for a new business card design i want it to be modern and sharp looking i usually order plastic business cards, and i would like to make the colors like the logo teal/charcoal i will like to have our services on icons with words.... our services are
ROOFING GUTTERS PAINTING PRESSURE WASHING EXTERIOR DESIGN & ATTIC VENTILATION. I also want to add my credentials

Target Market(s)

Oregon local market

Industry/Entity Type

Residential Construction

Contact Information for Business Card

Business info, services, number, website

Font styles to use
Serif
Sans Serif

Colors
33b8a4
5c5c5c
ffffff

Requirements
Must have
• Dale Finch
• Cell:
• Office:
• Email:
• Website:
• also i need our social media icons
• Services ROOFING GUTTERS PAINTING PRESSURE WASHING EXTERIOR DESIGN & ATTIC VENTILATION
• -icons for number, web, email, cell
• OR #584312
• Wa #KTRABLD461X7
Nice to have
• -Clean design Front & Back
• -Icons
• -shape House just like logo design
• -First Impression
Should not have
• Not Busy or lost of eye contact

```html
<!DOCTYPE html>
<html lang="en">
<head>
<meta charset="utf-8">
<title>Ridgeline Home Exteriors – Business Card</title>
<link href="https://fonts.googleapis.com/css2?family=Merriweather:wght@700;900&family=Open+Sans:wght@400;600&display=swap" rel="stylesheet">
<style>
  :root{
    --teal:#1d9a8b;
    --teal-light:#33b8a4;
    --charcoal:#5c5c5c;
    --charcoal-dark:#4a4a4a;
    --white:#ffffff;
    --page:#e9e9e7;
    --badge-red:#c8322c;
    --badge-grey:#9a9a9a;
    --badge-black:#1b1b1b;
  }
  *{box-sizing:border-box;margin:0;padding:0}
  html,body{width:1200px;height:900px;overflow:hidden;background:var(--page)}
  body{position:relative;font-family:'Open Sans',Arial,sans-serif}

  .card{position:absolute;left:250px;width:700px;height:400px;overflow:hidden;
        background:var(--white);box-shadow:0 6px 18px rgba(0,0,0,.18)}
  .card--back{top:36px}
  .card--front{top:464px}

  /* Back */
  .back__band{position:absolute;left:0;top:0;width:100%;height:250px;background:var(--teal)}
  .brand{position:absolute;display:flex;align-items:center;gap:12px}
  .brand__mark{width:22px;height:22px;flex:none}
  .brand__name{font-family:'Merriweather',Georgia,serif;font-weight:900;line-height:1.05;text-transform:uppercase}
  .brand--back{left:70px;top:88px}
  .brand--back .brand__mark{background:var(--white)}
  .brand--back .brand__name{color:var(--white);font-size:30px}
  .back__divider{position:absolute;left:330px;top:30px;width:1px;height:190px;background:rgba(255,255,255,.45)}
  .services{position:absolute;left:362px;top:62px;list-style:none;color:var(--white);
            font-size:17px;letter-spacing:.4px;line-height:21px}
  .services li{display:flex;align-items:center;gap:10px}
  .services li::before{content:"";width:7px;height:7px;border-radius:50%;background:var(--white)}
  .badges{position:absolute;left:0;top:250px;width:100%;height:150px;display:flex;
          justify-content:center;align-items:center;gap:44px}
  .badge{border-radius:4px}
  .badge--cert{width:170px;height:46px;background:linear-gradient(180deg,var(--badge-grey) 0 30%,var(--badge-red) 30% 100%)}
  .badge--listing{width:140px;height:50px;background:var(--badge-black);border-radius:6px}

  /* Front */
  .front__wave{position:absolute;left:0;top:0}
  .holder{position:absolute;left:60px;top:72px;font-family:'Merriweather',Georgia,serif;
          font-weight:900;font-size:28px;letter-spacing:.5px;text-transform:uppercase}
  .holder__first{color:var(--teal)}
  .holder__last{color:var(--charcoal)}
  .contacts{position:absolute;left:60px;top:162px;list-style:none;color:var(--charcoal-dark);font-size:19px;line-height:25px}
  .contacts li{display:flex;align-items:center;gap:8px}
  .contacts svg{width:16px;height:16px;flex:none;fill:var(--teal)}
  .licenses{position:absolute;left:82px;top:282px;color:var(--charcoal-dark);font-size:21px;line-height:27px}
  .brand--front{left:430px;top:52px;align-items:flex-start}
  .brand--front .brand__mark{background:var(--teal);margin-top:6px}
  .brand--front .brand__name{color:var(--teal);font-size:26px}
  .tagline{position:absolute;left:464px;top:150px;font-family:'Merriweather',Georgia,serif;font-weight:700;
           font-size:13px;letter-spacing:1px;color:var(--charcoal);text-transform:uppercase;
           border-top:2px solid var(--charcoal);padding-top:4px}
  .socials{position:absolute;right:40px;top:238px;display:flex;gap:6px}
  .socials span{width:22px;height:22px;border-radius:50%;background:var(--white)}
</style>
</head>
<body>

<section class="card card--back" aria-label="Card back">
  <div class="back__band"></div>
  <div class="brand brand--back">
    <span class="brand__mark"></span>
    <span class="brand__name">Ridgeline<br>Home<br>Exteriors</span>
  </div>
  <div class="back__divider"></div>
  <ul class="services">
    <li>ROOFING</li>
    <li>GUTTERS</li>
    <li>PAINTING</li>
    <li>PRESSURE WASHING</li>
    <li>EXTERIOR DESIGN &amp;</li>
    <li>ATTIC VENTILATION</li>
  </ul>
  <div class="badges">
    <div class="badge badge--cert" role="img" aria-label="Roofing contractor certification badge"></div>
    <div class="badge badge--listing" role="img" aria-label="Accredited business listing badge"></div>
  </div>
</section>

<section class="card card--front" aria-label="Card front">
  <svg class="front__wave" width="700" height="400" viewBox="0 0 700 400" aria-hidden="true">
    <path d="M0 372 C180 410 330 350 440 270 C520 212 600 190 700 186 L700 196 C610 200 530 228 455 284 C340 368 190 412 0 392 Z" fill="var(--charcoal)"/>
    <path d="M0 392 C190 412 340 368 455 284 C530 228 610 200 700 196 L700 400 L0 400 Z" fill="var(--white)"/>
    <path d="M0 400 C220 400 360 350 470 282 C540 238 610 210 700 206 L700 400 Z" fill="var(--teal)"/>
    <path d="M0 392 C150 404 300 380 420 315" fill="none" stroke="var(--white)" stroke-width="4"/>
  </svg>

  <h1 class="holder"><span class="holder__first">Dale</span> <span class="holder__last">Finch</span></h1>

  <ul class="contacts">
    <li><svg viewBox="0 0 16 16"><path d="M2 6c0-2 3-3 6-3s6 1 6 3v1h-3V5.5C10 5 6 5 5 5.5V7H2zM3 8h10l1 5H2z"/></svg>555-014 2087</li>
    <li><svg viewBox="0 0 16 16"><path d="M4 1h8v14H4zM5.5 2.5v9h5v-9zM7 12.5h2v1H7z"/></svg>555-014 3391</li>
    <li><svg viewBox="0 0 16 16"><path d="M1 3h14v10H1zM2 4.5v.3l6 4 6-4v-.3z"/></svg>info@ridgelinehome.com</li>
    <li><svg viewBox="0 0 16 16"><circle cx="8" cy="8" r="6.5"/></svg>www.ridgelinehome.com</li>
  </ul>

  <p class="licenses">OR #584312<br>Wa #KTRABLD461X7</p>

  <div class="brand brand--front">
    <span class="brand__mark"></span>
    <span class="brand__name">Ridgeline<br>Home Exteriors</span>
  </div>
  <p class="tagline">When Quality Matters.</p>

  <div class="socials" aria-label="Social media">
    <span></span><span></span><span></span><span></span>
  </div>
</section>

</body>
</html>
```